Need a business cards for a hair dressing salon.

Target Market(s)

Target woman for Hair cuts, bridal makeup, occasion, fashion makeup and etc.

Industry/Entity Type

Hair

Font styles to use
Serif
Script

Requirements
Must have
• - Business card to be memorable and recognizable

- Please include the following on the business card:
- Business name: Salon Orimba
- Name: Kalini Desmodo (Name Must be changeable)
- Occupation: Hair Dresser & Beautician
- Contact number: 04 739 2 HAIR
- Email: mail@orimba.com.au
- Facebook (please use image): www.facebook.com/orimba.com.au
Nice to have
• Font Styles:
Business Name - Script
Other Text - Serif

```html
<!DOCTYPE html>
<html lang="en">
<head>
<meta charset="utf-8">
<title>Salon Orimba – Business Cards</title>
<link rel="stylesheet" href="https://fonts.googleapis.com/css2?family=Montserrat:wght@600&family=Questrial&display=swap">
<style>
  :root {
    --backdrop: #e9e9ee;
    --rose: #b5625a;
    --paper: #fbfbfb;
    --ink: #3b3b3b;
    --ink-soft: #555555;
    --on-rose: #ffffff;
    --rose-mark: rgba(255, 255, 255, 0.12);
    --paper-mark: rgba(160, 168, 175, 0.16);
  }
  * { box-sizing: border-box; margin: 0; padding: 0; }
  html, body {
    width: 1200px;
    height: 934px;
    overflow: hidden;
    background: var(--backdrop);
    font-family: "Questrial", "Century Gothic", sans-serif;
  }
  .stage { position: relative; width: 1200px; height: 934px; }

  .brand-title {
    position: absolute;
    top: 70px;
    right: 100px;
    font-size: 54px;
    color: var(--ink);
    letter-spacing: 1px;
  }

  .card {
    position: absolute;
    width: 540px;
    height: 308px;
    overflow: hidden;
    box-shadow: 0 6px 18px rgba(0, 0, 0, 0.12);
  }
  .card--rose { left: 70px; top: 250px; background: var(--rose); color: var(--on-rose); }
  .card--paper { left: 600px; top: 470px; background: var(--paper); color: var(--ink); }

  .card__mark {
    position: absolute;
    left: 30px;
    top: 20px;
    width: 170px;
    height: 170px;
    border-radius: 50%;
  }
  .card--rose .card__mark { background: var(--rose-mark); }
  .card--paper .card__mark { background: var(--paper-mark); }

  .card__brand {
    position: absolute;
    top: 44px;
    right: 38px;
    font-size: 38px;
    letter-spacing: 0.5px;
  }

  .card__contact {
    position: absolute;
    left: 30px;
    bottom: 30px;
    display: flex;
    align-items: stretch;
    gap: 10px;
    font-size: 14px;
    line-height: 18px;
  }
  .card__icons {
    display: flex;
    flex-direction: column;
    justify-content: flex-end;
    gap: 4px;
    padding-top: 14px;
  }
  .card__icons svg { width: 12px; height: 12px; display: block; }
  .card__icons .dot { width: 8px; height: 8px; border-radius: 50%; margin-left: 2px; background: currentColor; }
  .card__divider { width: 1px; background: currentColor; opacity: 0.7; }
  .card__lines { list-style: none; }

  .card__person {
    position: absolute;
    right: 34px;
    bottom: 96px;
    text-align: right;
  }
  .card__name {
    font-family: "Montserrat", "Century Gothic", sans-serif;
    font-weight: 600;
    font-size: 17px;
    letter-spacing: 0.8px;
    text-transform: uppercase;
  }
  .card__role { font-size: 13px; color: inherit; opacity: 0.9; margin-top: 2px; }
</style>
</head>
<body>
<main class="stage">
  <h1 class="brand-title">Salon Orimba</h1>

  <section class="card card--rose" aria-label="Business card, rose colourway">
    <div class="card__mark" aria-hidden="true"></div>
    <p class="card__brand">Salon Orimba</p>
    <div class="card__person">
      <p class="card__name">Kalini Desmodo</p>
      <p class="card__role">Hair Dresser &amp; Beautician</p>
    </div>
    <div class="card__contact">
      <div class="card__icons">
        <svg viewBox="0 0 12 12" aria-hidden="true"><path fill="currentColor" d="M2.4 0.8l1.8 2.4-1 1.1c0.6 1.5 1.9 2.8 3.5 3.5l1.1-1 2.4 1.8-0.8 2.1C5 10.4 1.6 7 0.4 1.6z"/></svg>
        <svg viewBox="0 0 12 12" aria-hidden="true"><rect x="0.5" y="2.5" width="11" height="7" fill="none" stroke="currentColor"/><path d="M0.5 2.5l5.5 4 5.5-4" fill="none" stroke="currentColor"/></svg>
        <span class="dot" aria-hidden="true"></span>
      </div>
      <div class="card__divider"></div>
      <ul class="card__lines">
        <li>04 739 2 HAIR</li>
        <li>mail@orimba.com.au</li>
        <li>/orimba.com.au</li>
      </ul>
    </div>
  </section>

  <section class="card card--paper" aria-label="Business card, white colourway">
    <div class="card__mark" aria-hidden="true"></div>
    <p class="card__brand">Salon Orimba</p>
    <div class="card__person">
      <p class="card__name">Kalini Desmodo</p>
      <p class="card__role">Hair Dresser &amp; Beautician</p>
    </div>
    <div class="card__contact">
      <div class="card__icons">
        <svg viewBox="0 0 12 12" aria-hidden="true"><path fill="currentColor" d="M2.4 0.8l1.8 2.4-1 1.1c0.6 1.5 1.9 2.8 3.5 3.5l1.1-1 2.4 1.8-0.8 2.1C5 10.4 1.6 7 0.4 1.6z"/></svg>
        <svg viewBox="0 0 12 12" aria-hidden="true"><rect x="0.5" y="2.5" width="11" height="7" fill="none" stroke="currentColor"/><path d="M0.5 2.5l5.5 4 5.5-4" fill="none" stroke="currentColor"/></svg>
        <span class="dot" aria-hidden="true"></span>
      </div>
      <div class="card__divider"></div>
      <ul class="card__lines">
        <li>04 739 2 HAIR</li>
        <li>mail@orimba.com.au</li>
        <li>/orimba.com.au</li>
      </ul>
    </div>
  </section>
</main>
</body>
</html>
```